Business card and stationary for a consultant firm
Sharp Compass
Professional
Renske Hoorneman
Zwaluwlaan 38
Curaçao
Renskehoorneman@postvlek.com
Zwaluwlaan38

```html
<!DOCTYPE html>
<html lang="en">
<head>
<meta charset="utf-8">
<title>Sharp Compass – Business Card</title>
<link rel="stylesheet" href="https://fonts.googleapis.com/css2?family=Crimson+Text:wght@400;600&display=swap">
<style>
  :root {
    --card-white: #ffffff;
    --swoosh-grey: #b3b3b3;
    --panel-black: #000000;
    --ink: #111111;
    --ink-light: #ffffff;
    --mark: #3a8fc9;
  }
  html, body {
    margin: 0;
    padding: 0;
    width: 1200px;
    height: 778px;
    overflow: hidden;
    background: var(--card-white);
  }
  .card {
    position: relative;
    width: 1200px;
    height: 778px;
    background: var(--card-white);
    font-family: "Crimson Text", Georgia, serif;
    color: var(--ink);
    overflow: hidden;
  }
  .card__swoosh {
    position: absolute;
    inset: 0;
    width: 1200px;
    height: 778px;
  }
  .swoosh-grey { fill: var(--swoosh-grey); }
  .swoosh-black { fill: var(--panel-black); }

  .brand {
    position: absolute;
    left: 100px;
    top: 118px;
    display: flex;
    align-items: center;
    gap: 28px;
  }
  .brand__dot {
    width: 96px;
    height: 96px;
    border-radius: 50%;
    background: var(--mark);
  }
  .brand__name {
    font-size: 62px;
    font-weight: 600;
    color: var(--ink);
    letter-spacing: 0.5px;
    line-height: 1;
  }

  .contact {
    position: absolute;
    left: 84px;
    top: 428px;
    font-size: 29px;
    line-height: 58px;
    color: var(--ink);
  }
  .contact__line {
    display: flex;
    align-items: center;
    gap: 10px;
    white-space: nowrap;
  }
  .contact__icon {
    width: 20px;
    height: 20px;
    flex: none;
  }
  .contact__icon path,
  .contact__icon rect {
    fill: none;
    stroke: var(--ink);
    stroke-width: 1.8;
  }

  .person {
    position: absolute;
    right: 70px;
    top: 598px;
    text-align: right;
    color: var(--ink-light);
  }
  .person__name {
    font-size: 46px;
    font-weight: 400;
    line-height: 1.1;
  }
  .person__title {
    font-size: 31px;
    line-height: 1.3;
  }
</style>
</head>
<body>
  <main class="card">
    <svg class="card__swoosh" viewBox="0 0 1200 778" aria-hidden="true">
      <path class="swoosh-grey" d="M795 0 C1150 110 1080 520 330 778 L1200 778 L1200 0 Z"/>
      <path class="swoosh-black" d="M955 0 C1240 190 1040 560 380 778 L1200 778 L1200 0 Z"/>
    </svg>

    <header class="brand">
      <span class="brand__dot"></span>
      <span class="brand__name">Sharp Compass</span>
    </header>

    <section class="contact">
      <div class="contact__line">Zwaluwlaan 38</div>
      <div class="contact__line">Curaçao</div>
      <div class="contact__line">
        <svg class="contact__icon" viewBox="0 0 20 20" aria-hidden="true">
          <rect x="6" y="2" width="8" height="16" rx="1.5"/>
        </svg>
        (599-9) 5550147
      </div>
      <div class="contact__line">
        <svg class="contact__icon" viewBox="0 0 20 20" aria-hidden="true">
          <rect x="2" y="5" width="16" height="11"/>
          <path d="M2 5 L10 11 L18 5"/>
        </svg>
        Renskehoorneman@postvlek.com
      </div>
    </section>

    <section class="person">
      <div class="person__name">Renske Hoorneman</div>
      <div class="person__title">Managing Director</div>
    </section>
  </main>
</body>
</html>
```